Business Card

Please design a business card with our logo on a cream coloured background and include the following information:

Tallowmere Shopping Centre
ph (08) 9341 7086

sales@velvetpetalblooms.com

www.velvetpetalblooms.com

on reverse:

Find us on Friendloop
friendloop.com/velvetpetalblooms

```html
<!DOCTYPE html>
<html lang="en">
<head>
<meta charset="utf-8">
<title>Velvet Petal Blooms – Business Card</title>
<link rel="stylesheet" href="https://fonts.googleapis.com/css2?family=Fira+Sans:wght@400;500&family=Fira+Sans+Condensed:wght@500&display=swap">
<style>
  :root {
    --backdrop: #2a2a2a;
    --cream: #e2cda2;
    --cream-light: #e9d7b1;
    --leaf-green: #5b8a2f;
    --ink: #3c3c3c;
  }
  html, body {
    margin: 0;
    width: 1200px;
    height: 896px;
    overflow: hidden;
    background: var(--backdrop);
  }
  .canvas {
    position: relative;
    width: 1200px;
    height: 896px;
  }
  .card {
    position: absolute;
    left: 353px;
    width: 485px;
    height: 268px;
    background: linear-gradient(135deg, var(--cream-light), var(--cream));
    color: var(--ink);
    font-family: "Fira Sans", sans-serif;
    text-align: center;
  }
  .card--back { top: 165px; }
  .card--front { top: 473px; }

  .brand-mark {
    position: absolute;
    left: 0;
    right: 0;
    display: flex;
    align-items: center;
    justify-content: center;
    gap: 12px;
  }
  .card--back .brand-mark { top: 96px; }
  .card--front .brand-mark { top: 28px; }
  .brand-mark__dot {
    width: 22px;
    height: 22px;
    border-radius: 50%;
    background: var(--leaf-green);
  }
  .card--front .brand-mark__dot {
    width: 42px;
    height: 42px;
  }
  .brand-mark__name {
    font-size: 24px;
    font-weight: 500;
    color: var(--leaf-green);
  }

  .rule {
    position: absolute;
    left: 119px;
    width: 246px;
    height: 0;
    border-top: 1.5px solid var(--leaf-green);
  }
  .card--back .rule { top: 201px; }
  .card--front .rule { top: 181px; }

  .social {
    position: absolute;
    top: 210px;
    left: 0;
    right: 0;
    margin: 0;
    font-size: 15px;
    line-height: 18px;
  }
  .business-name {
    position: absolute;
    top: 89px;
    left: 0;
    right: 0;
    margin: 0;
    font-family: "Fira Sans Condensed", sans-serif;
    font-weight: 500;
    font-size: 28px;
    color: var(--ink);
  }
  .location {
    position: absolute;
    top: 151px;
    left: 0;
    right: 0;
    font-size: 15.5px;
    letter-spacing: 0.6px;
    text-transform: uppercase;
  }
  .contact {
    position: absolute;
    top: 192px;
    left: 0;
    right: 0;
    margin: 0;
    padding: 0;
    list-style: none;
    font-size: 13.5px;
    line-height: 21px;
  }
</style>
</head>
<body>
<main class="canvas">
  <section class="card card--back" aria-label="Card reverse">
    <div class="brand-mark">
      <span class="brand-mark__dot"></span>
      <span class="brand-mark__name">Velvet Petal Blooms</span>
    </div>
    <div class="rule"></div>
    <p class="social">Find us on Friendloop<br>friendloop.com/velvetpetalblooms</p>
  </section>

  <section class="card card--front" aria-label="Card front">
    <div class="brand-mark"><span class="brand-mark__dot"></span></div>
    <h1 class="business-name">Velvet Petal Blooms</h1>
    <div class="location">Tallowmere Shopping Centre</div>
    <div class="rule"></div>
    <ul class="contact">
      <li>(08) 9341 7086</li>
      <li>sales@velvetpetalblooms.com</li>
      <li>www.velvetpetalblooms.com</li>
    </ul>
  </section>
</main>
</body>
</html>
```